Fernvale Craft Works business card design- Fine Art sculpture business (Contract guaranteed)

This business card is for a fine art business. Though we don't have a website up and running yet it should be up soon. I would like the business card to be elegant and fairly simple with a picture of one of my sculptures on the front (you might need to photoshop out the background) as well as my basic contact info (my name,phone # and e-mail). On the back I'd like it to be pretty simple with just "Notes" and some blank lines for writing in info.

Target Market(s)

High end artwork buyers

Industry/Entity Type

Art Gallery

Contact Information for Business Card

Marlo Prewitt Phone: (555) 213-4098 E-mail: marlo@quillbrookmail.com Facebook: @fernvalecraftworks Instagram: fernvalecraftworks

Colors

Designer to choose colors to be used in the design.

Requirements
Must have
• *A picture of one of my sculptures*, my name, business name (Fernvale Craft Works), e-mail, phone #, and a notes section on the back.
• Fernvale Craft Works
• Marlo Prewitt
• (555)213-4098
• marlo@quillbrookmail.com
• Facebook: @fernvalecraftworks
• Instagram: fernvalecraftworks
Nice to have
• It'd be nice if you can crop out the background in the sculpture pictures, which ever one you end up using.

```html
<!DOCTYPE html>
<html lang="en">
<head>
<meta charset="UTF-8">
<title>Fernvale Craft Works – Business Card</title>
<link rel="stylesheet" href="https://fonts.googleapis.com/css2?family=Lato:wght@400;700&display=swap">
<style>
  :root {
    --backdrop: #6a4479;
    --card-white: #f7f6f8;
    --panel-purple: #8a52b6;
    --panel-purple-deep: #7c47a8;
    --notes-ink: #a37dc8;
    --rule-line: #a885c9;
    --photo-black: #262626;
    --text-white: #ffffff;
    --text-soft: #e6d8f2;
  }
  * { box-sizing: border-box; margin: 0; padding: 0; }
  html, body {
    width: 1200px;
    height: 750px;
    overflow: hidden;
  }
  body {
    background: var(--backdrop);
    font-family: "Lato", sans-serif;
    display: flex;
    align-items: center;
    justify-content: center;
    gap: 48px;
  }
  .card {
    width: 540px;
    height: 372px;
    background: var(--card-white);
    padding: 20px;
    box-shadow: 0 10px 28px rgba(30, 10, 40, 0.35);
  }
  .card-panel {
    position: relative;
    width: 100%;
    height: 100%;
    background: linear-gradient(160deg, var(--panel-purple), var(--panel-purple-deep));
    overflow: hidden;
  }

  /* Back: notes */
  .notes-title {
    position: absolute;
    top: 44px;
    left: 0;
    right: 0;
    text-align: center;
    color: var(--notes-ink);
    font-size: 34px;
    font-weight: 700;
    letter-spacing: 0.5px;
  }
  .notes-lines {
    position: absolute;
    left: 70px;
    right: 40px;
    top: 112px;
  }
  .notes-line {
    height: 1px;
    background: var(--rule-line);
    margin-bottom: 48px;
  }

  /* Front: sculpture & contact */
  .business-name {
    position: absolute;
    top: 26px;
    left: 34px;
    color: var(--text-white);
    font-size: 19px;
    font-weight: 700;
    letter-spacing: 0.5px;
  }
  .sculpture-frame {
    position: absolute;
    top: 0;
    right: 0;
    width: 230px;
    height: 175px;
  }
  .contact {
    position: absolute;
    left: 34px;
    bottom: 28px;
    color: var(--text-white);
  }
  .contact-phone,
  .contact-email {
    font-size: 17px;
    line-height: 1.35;
  }
  .contact-social {
    font-size: 14px;
    line-height: 1.4;
    color: var(--text-soft);
  }
  .contact-social span + span { margin-left: 14px; }
  .contact-name {
    margin-top: 6px;
    font-size: 38px;
    font-weight: 700;
    line-height: 1.1;
  }
</style>
</head>
<body>

  <section class="card card-back" aria-label="Card back">
    <div class="card-panel">
      <h2 class="notes-title">Notes</h2>
      <div class="notes-lines">
        <div class="notes-line"></div>
        <div class="notes-line"></div>
        <div class="notes-line"></div>
      </div>
    </div>
  </section>

  <section class="card card-front" aria-label="Card front">
    <div class="card-panel">
      <p class="business-name">Fernvale Craft Works</p>
      <svg class="sculpture-frame" viewBox="0 0 230 175" role="img" aria-label="Photograph of an amethyst geode arch sculpture on a stone base">
        <defs>
          <linearGradient id="amethyst" x1="0" y1="0" x2="1" y2="1">
            <stop offset="0" stop-color="#5b3d8f"/>
            <stop offset="0.5" stop-color="#7a5ab8"/>
            <stop offset="1" stop-color="#3f2c6a"/>
          </linearGradient>
        </defs>
        <polygon points="40,0 230,0 230,175 0,175" fill="var(--photo-black)"/>
        <rect x="75" y="18" width="135" height="142" rx="40" fill="url(#amethyst)" opacity="0.85"/>
      </svg>
      <div class="contact">
        <p class="contact-phone">(555) 213-4098</p>
        <p class="contact-email">marlo@quillbrookmail.com</p>
        <p class="contact-social"><span>Facebook: @fernvalecraftworks</span><span>Instagram: fernvalecraftworks</span></p>
        <h1 class="contact-name">Marlo Prewitt</h1>
      </div>
    </div>
  </section>

</body>
</html>
```